New Managed IT company needs a business card

We are an IT management and support company that needs a business card design. I have a logo that I'll provide. Blues and blacks match the logo, but i'm open to anything. I want the card to help people take us seriously, but still have some energy and fun in it. The card should communicate stability and a solid company.

Target Market(s)

Target market includes Owners and Presidents at small businesses of 20 - 100 employees in the Pittsburgh PA area.

Industry/Entity Type

Information Technology

Contact Information for Business Card

i am open to other designs, but i imagine having only the logo on one side and then the logo plus all contact details on the other side.

Requirements
Must have
• Our logo
• Company name is optional if the logo makes it obvious
• A name - Cole Perrin
• A title - President
• A phone number - 724-XXX-XXXX
• A mobile phone number - 724-615-2748
• An email address - cperrin@techvaultgrid.com
• a website - techvaultgrid.com or www.techvaultgrid.com
Nice to have
• some people tell me the logo feels like a superhero theme, some fun with that idea might be good. I'm open to ideas.
Should not have
• stock photos of people or computers - especially old looking stuff.

```html
<!DOCTYPE html>
<html lang="en">
<head>
<meta charset="UTF-8">
<title>TechVault Grid – Business Card</title>
<link rel="stylesheet" href="https://fonts.googleapis.com/css2?family=Michroma&family=Montserrat:wght@400;600;700&display=swap">
<style>
  :root {
    --canvas-bg: #3a312d;
    --card-white: #f4f5f6;
    --card-dark: #2b2b2c;
    --ink-dark: #1d1f22;
    --ink-body: #2c2e31;
    --brand-blue: #1377c9;
    --brand-blue-light: #1a9be6;
    --mark-dark: #1e1f21;
    --emboss: #1b1b1c;
  }
  * { margin: 0; padding: 0; box-sizing: border-box; }
  html, body {
    width: 1200px; height: 716px; overflow: hidden;
    background: var(--canvas-bg);
  }
  .stage {
    position: relative; width: 1200px; height: 716px;
    display: flex; align-items: center; justify-content: center; gap: 40px;
  }
  .card {
    position: relative; width: 500px; height: 286px;
    border-radius: 10px; overflow: hidden;
    box-shadow: 0 14px 30px rgba(0,0,0,0.45);
  }
  .card-front { background: var(--card-white); }
  .card-back { background: var(--card-dark); }

  /* front */
  .front-brand {
    position: absolute; left: 34px; top: 26px;
    display: flex; flex-direction: column; align-items: center; gap: 5px;
  }
  .brand-dot { width: 22px; height: 22px; border-radius: 50%; background: var(--brand-blue); }
  .brand-name {
    font-family: "Michroma", sans-serif; font-size: 9px; letter-spacing: 1px;
    color: var(--ink-dark); text-transform: uppercase; line-height: 1.2; text-align: center;
  }
  .person { position: absolute; left: 34px; top: 96px; }
  .person-name {
    font-family: "Michroma", sans-serif; font-size: 17px; letter-spacing: 1.5px;
    color: var(--ink-dark); text-transform: uppercase;
  }
  .person-title {
    font-family: "Montserrat", sans-serif; font-weight: 700; font-size: 10px;
    letter-spacing: 2px; color: var(--brand-blue); text-transform: uppercase; margin-top: 2px;
  }
  .contact-list {
    position: absolute; left: 34px; top: 146px; list-style: none;
    font-family: "Montserrat", sans-serif; font-size: 11.5px; color: var(--ink-body);
  }
  .contact-list li { display: flex; align-items: center; gap: 9px; height: 19px; }
  .contact-icon { width: 11px; height: 11px; fill: var(--ink-dark); flex: none; }
  .contact-icon.blue { fill: var(--brand-blue); }

  .edge-circle { position: absolute; width: 200px; height: 200px; top: 60px; }
  .card-front .edge-circle { right: -100px; }
  .card-back .edge-circle { left: -100px; }

  /* back */
  .back-lockup {
    position: absolute; right: 40px; top: 118px;
    display: flex; align-items: center; gap: 14px;
  }
  .back-dot { width: 46px; height: 46px; border-radius: 50%; background: var(--brand-blue-light); }
  .back-name {
    font-family: "Michroma", sans-serif; font-size: 22px; letter-spacing: 2px;
    color: var(--emboss); text-transform: uppercase; line-height: 1.15;
  }
</style>
</head>
<body>
<main class="stage">
  <section class="card card-front" aria-label="Card front">
    <div class="front-brand">
      <span class="brand-dot"></span>
      <span class="brand-name">TechVault<br>Grid</span>
    </div>
    <div class="person">
      <h1 class="person-name">Cole Perrin</h1>
      <p class="person-title">President</p>
    </div>
    <ul class="contact-list">
      <li>
        <svg class="contact-icon blue" viewBox="0 0 12 12"><path d="M2 1h3l1 3-2 1a7 7 0 0 0 3 3l1-2 3 1v3c0 1-1 1-1 1A10 10 0 0 1 1 2s0-1 1-1z"/></svg>
        724-XXX-XXXX
      </li>
      <li>
        <svg class="contact-icon blue" viewBox="0 0 12 12"><rect x="3" y="0.5" width="6" height="11" rx="1"/><rect x="4" y="2" width="4" height="7" fill="#f4f5f6"/></svg>
        724-615-2748
      </li>
      <li>
        <svg class="contact-icon blue" viewBox="0 0 12 12"><rect x="0.5" y="2" width="11" height="8" rx="1"/><path d="M1 3l5 4 5-4" stroke="#f4f5f6" stroke-width="1" fill="none"/></svg>
        cperrin@techvaultgrid.com
      </li>
      <li>
        <svg class="contact-icon" viewBox="0 0 12 12"><circle cx="6" cy="6" r="5.2" fill="none" stroke="#1d1f22" stroke-width="1"/><ellipse cx="6" cy="6" rx="2.3" ry="5.2" fill="none" stroke="#1d1f22" stroke-width="0.9"/><path d="M1 6h10" stroke="#1d1f22" stroke-width="0.9"/></svg>
        www.techvaultgrid.com
      </li>
    </ul>
    <svg class="edge-circle" viewBox="0 0 200 200" aria-hidden="true"><circle cx="100" cy="100" r="100" fill="var(--mark-dark)"/></svg>
  </section>

  <section class="card card-back" aria-label="Card back">
    <svg class="edge-circle" viewBox="0 0 200 200" aria-hidden="true"><circle cx="100" cy="100" r="100" fill="var(--mark-dark)"/></svg>
    <div class="back-lockup">
      <span class="back-dot"></span>
      <span class="back-name">TechVault<br>Grid</span>
    </div>
  </section>
</main>
</body>
</html>
```